Bobcat / excavator / tipper contractor
info for back of card {
2.3 ton bobcat 1.6m wide
3.6 ton excavator 1.6 wide
4.5M tipper 2.4 wide }
In the industry since 1999
Experienced in all aspects of bobcat excavator general hire work
Brisbane to goldcoast area
competitive rates

As for the image uploaded, I kind of like the H made out of the bulidings and the brown and yellow are the colors of my footy team. but open to anything that is unique the portrays excavation that can become a symbol for my business.so the H is good or something with CTS.

Im wanting to create business cards and either large magnets or a wrap for the front of the truck.
corbintrench @ mailvex . com

Contractor

Reid Corbin
Corbin Trench Services Pty Ltd
ABN 52830174926
mobile 0491286304
corbintrench@mailvex.com

```html
<!DOCTYPE html>
<html lang="en">
<head>
<meta charset="utf-8">
<title>Corbin Trench Services – Business Card</title>
<link rel="stylesheet" href="https://fonts.googleapis.com/css2?family=Oswald:wght@500;700&family=Roboto+Condensed:wght@400;700&display=swap">
<style>
  :root {
    --canvas: #e9e6e1;
    --card-black: #0c0c0c;
    --panel-grey: #262626;
    --rule-grey: #3a3a3a;
    --brand-brown: #8b4a1d;
    --brand-yellow: #e6c21b;
    --ink-white: #f4f4f4;
  }
  * { box-sizing: border-box; margin: 0; padding: 0; }
  html, body { width: 1200px; height: 900px; overflow: hidden; }
  body {
    background: var(--canvas);
    font-family: "Roboto Condensed", "Arial Narrow", sans-serif;
    position: relative;
  }
  .card {
    position: absolute;
    left: 273px;
    width: 654px;
    height: 400px;
    background: var(--card-black);
    overflow: hidden;
    box-shadow: 0 6px 18px rgba(0,0,0,0.18);
  }
  .card--front { top: 40px; }
  .card--back { top: 470px; }

  /* Brand lockup */
  .brand-mark {
    display: flex;
    align-items: center;
    gap: 10px;
  }
  .brand-mark__square {
    width: 22px; height: 22px;
    background: var(--brand-yellow);
  }
  .brand-mark__name {
    font-family: "Oswald", "Arial Narrow", sans-serif;
    font-weight: 700;
    font-size: 44px;
    letter-spacing: 2px;
    color: var(--brand-brown);
    line-height: 1;
  }
  .company-name {
    font-family: "Oswald", "Arial Narrow", sans-serif;
    font-weight: 700;
    color: var(--brand-brown);
    text-transform: uppercase;
    line-height: 1;
    letter-spacing: 0.5px;
  }
  .trade-line {
    font-family: "Oswald", "Arial Narrow", sans-serif;
    font-weight: 500;
    color: var(--brand-yellow);
    text-transform: uppercase;
    letter-spacing: 0.5px;
    line-height: 1;
  }

  /* Front */
  .front__identity {
    position: absolute;
    left: 0; top: 0;
    width: 100%; height: 250px;
    display: flex;
    flex-direction: column;
    align-items: center;
    justify-content: center;
    gap: 16px;
  }
  .front__identity .company-name { font-size: 30px; }
  .front__identity .trade-line { font-size: 16px; margin-top: -6px; }
  .front__band {
    position: absolute;
    left: 0; bottom: 0;
    width: 100%; height: 150px;
    background: var(--brand-brown);
    border-top: 3px solid #1e1e1e;
    display: flex;
    align-items: center;
    justify-content: center;
    gap: 22px;
  }
  .person { text-align: right; }
  .person__name {
    font-family: "Oswald", "Arial Narrow", sans-serif;
    font-weight: 700;
    font-size: 28px;
    text-transform: uppercase;
    line-height: 1;
    color: var(--brand-yellow);
  }
  .person__name .surname { color: var(--ink-white); }
  .person__role {
    font-family: "Oswald", "Arial Narrow", sans-serif;
    font-weight: 500;
    font-size: 16px;
    color: var(--brand-yellow);
    text-transform: uppercase;
    margin-top: 4px;
  }
  .band-divider {
    width: 3px; height: 76px;
    background: var(--brand-yellow);
  }
  .contact-list { list-style: none; font-size: 20px; line-height: 1.3; color: var(--ink-white); }
  .contact-list .label { color: var(--brand-yellow); }

  /* Back */
  .back__identity {
    position: absolute;
    right: 34px; top: 30px;
    text-align: right;
    display: flex;
    flex-direction: column;
    align-items: flex-end;
    gap: 10px;
  }
  .back__identity .brand-mark { margin-right: 90px; margin-bottom: 4px; }
  .back__identity .company-name { font-size: 30px; }
  .back__identity .trade-line { font-size: 16px; }
  .fleet-list {
    position: absolute;
    right: 34px; top: 182px;
    list-style: none;
    text-align: right;
  }
  .fleet-list li {
    font-family: "Roboto Condensed", "Arial Narrow", sans-serif;
    font-size: 17px;
    letter-spacing: 1px;
    text-transform: uppercase;
    color: var(--brand-yellow);
    line-height: 1.35;
  }
  .back__rules {
    position: absolute;
    left: 0; top: 0;
    width: 654px; height: 400px;
  }
  .back__panel {
    position: absolute;
    left: 0; bottom: 0;
    width: 100%; height: 120px;
    background: var(--panel-grey);
    padding: 16px 34px 0 0;
    text-align: right;
    color: var(--ink-white);
  }
  .back__panel .since {
    font-family: "Oswald", "Arial Narrow", sans-serif;
    font-weight: 700;
    font-size: 20px;
    color: var(--brand-yellow);
    text-transform: uppercase;
    letter-spacing: 0.5px;
    margin-bottom: 4px;
  }
  .back__panel p { font-size: 16px; line-height: 1.3; }
</style>
</head>
<body>

  <section class="card card--front" aria-label="Business card front">
    <div class="front__identity">
      <div class="brand-mark">
        <span class="brand-mark__square"></span>
        <span class="brand-mark__name">CTS</span>
      </div>
      <h1 class="company-name">Corbin Trench Services Pty Ltd</h1>
      <p class="trade-line">Bobcat / Excavator / Tipper Contractor</p>
    </div>
    <div class="front__band">
      <div class="person">
        <p class="person__name">Reid <span class="surname">Corbin</span></p>
        <p class="person__role">Director</p>
      </div>
      <span class="band-divider"></span>
      <ul class="contact-list">
        <li><span class="label">ABN :</span> 52830174926</li>
        <li><span class="label">Mobile :</span> 0491286304</li>
        <li>corbintrench@mailvex.com</li>
      </ul>
    </div>
  </section>

  <section class="card card--back" aria-label="Business card back">
    <svg class="back__rules" viewBox="0 0 654 400" aria-hidden="true">
      <g stroke="var(--rule-grey)" stroke-width="1.5" fill="none">
        <line x1="0" y1="210" x2="654" y2="210"/>
        <line x1="0" y1="233" x2="654" y2="233"/>
        <line x1="0" y1="256" x2="654" y2="256"/>
        <line x1="0" y1="276" x2="654" y2="276"/>
      </g>
    </svg>
    <div class="back__identity">
      <div class="brand-mark">
        <span class="brand-mark__square"></span>
        <span class="brand-mark__name">CTS</span>
      </div>
      <h2 class="company-name">Corbin Trench Services Pty Ltd</h2>
      <p class="trade-line">Bobcat / Excavator / Tipper Contractor</p>
    </div>
    <ul class="fleet-list">
      <li>2.3 Ton Bobcat 1.6m wide</li>
      <li>3.6 Ton Excavator 1.6 wide</li>
      <li>4.5m Tipper 2.4 wide</li>
    </ul>
    <div class="back__panel">
      <p class="since">In the industry since 1999</p>
      <p>Experienced in all aspects of bobcat excavator general hire work</p>
      <p>Brisbane to GOLDCOAST area</p>
      <p>Competitive rates</p>
    </div>
  </section>

</body>
</html>
```